Prepare a modern, professional business card for Meridel Vantage Advisory (MVA) Our company is in the banking, compliance and finance industry. We provide kiosks, software integration, and compliance guidelines so that banks can "bank" Marijuana Dispensaries with MonLex, Office of Statute Review and NBRA approval.

Target Market(s)

Banks

Industry/Entity Type

Business

Contact Information for Business Card

Peter L Oakridge
Meridel Vantage Advisory
Vice President
4427 Larkspur Crossing Way
Suite 218
Larkhaven, NR 40217
pete@mvalq.com
555-418-7362

Font styles to use
Sans Serif

Requirements
Nice to have
• I like the clean simple appearance of Quince computers. Perhaps the three LETTERS of MVA can be the LOGO on the Card and the Company name could be incorporated in the contact information. Like colors of white, black and gray

```html
<!DOCTYPE html>
<html lang="en">
<head>
<meta charset="utf-8">
<title>Meridel Vantage Advisory — Business Card Variants</title>
<link rel="stylesheet" href="https://fonts.googleapis.com/css2?family=Exo+2:ital,wght@0,300;0,400;0,600;0,700;1,300&display=swap">
<style>
  :root {
    --paper: #ffffff;
    --ink-black: #0d0d0d;
    --steel: #7b7676;
    --steel-soft: #a9a5a5;
    --mist: #d9d7d7;
    --mark: #6f6b6b;
    --mark-dark: #5f5c5c;
    --text-grey: #8e8b8b;
    --text-dark: #5a5757;
    --text-light: #c9c6c6;
  }
  * { margin: 0; padding: 0; box-sizing: border-box; }
  html, body {
    width: 1200px;
    height: 602px;
    overflow: hidden;
    background: var(--paper);
    font-family: "Exo 2", sans-serif;
  }
  .card-sheet {
    position: relative;
    width: 1200px;
    height: 602px;
  }
  .card {
    position: absolute;
    top: 0;
    width: 344px;
    height: 602px;
    overflow: hidden;
  }
  .card--light {
    left: 0;
    background: linear-gradient(157deg, var(--paper) 0%, var(--paper) 46%, var(--mist) 62%, var(--steel-soft) 80%, var(--steel) 100%);
  }
  .card--fade {
    left: 410px;
    width: 346px;
    background: linear-gradient(157deg, var(--steel) 0%, var(--steel-soft) 28%, var(--mist) 44%, var(--paper) 58%, var(--paper) 100%);
  }
  .card--dark {
    left: 857px;
    width: 343px;
    background: linear-gradient(150deg, #6a6767 0%, #3a3838 22%, #151414 44%, var(--ink-black) 60%, var(--ink-black) 100%);
  }
  .brand-mark {
    position: absolute;
    left: 8px;
    top: 2px;
    font-size: 98px;
    font-weight: 700;
    letter-spacing: -2px;
    line-height: 1;
    color: var(--mark);
  }
  .card--dark .brand-mark { color: var(--mark-dark); }
  .contact {
    position: absolute;
    right: 9px;
    top: 454px;
    text-align: right;
    color: var(--text-dark);
  }
  .contact__name {
    font-size: 13px;
    font-weight: 600;
    line-height: 16px;
  }
  .contact__title {
    font-size: 10.5px;
    font-weight: 300;
    line-height: 13px;
    margin-bottom: 14px;
  }
  .contact__address,
  .contact__reach {
    font-size: 10px;
    font-style: italic;
    font-weight: 300;
    line-height: 13px;
  }
  .contact__reach { margin-top: 11px; }
  .company-name {
    position: absolute;
    left: 10px;
    bottom: 6px;
    font-size: 20px;
    font-weight: 400;
    color: var(--text-grey);
    white-space: nowrap;
  }
  .card--light .contact,
  .card--light .company-name { color: var(--paper); }
  .card--fade .contact { color: var(--text-dark); }
  .card--dark .contact { color: var(--text-light); }
</style>
</head>
<body>
<main class="card-sheet">
  <section class="card card--light" aria-label="Business card, white and grey">
    <div class="brand-mark">MVA</div>
    <div class="contact">
      <p class="contact__name">Peter L Oakridge</p>
      <p class="contact__title">Vice President</p>
      <p class="contact__address">4427 Larkspur Crossing Way Suite<br>218 Larkhaven, NR 40217</p>
      <p class="contact__reach">pete@mvalq.com 555-418-7362</p>
    </div>
    <p class="company-name">Meridel Vantage Advisory</p>
  </section>

  <section class="card card--fade" aria-label="Business card, grey fading to white">
    <div class="brand-mark">MVA</div>
    <div class="contact">
      <p class="contact__name">Peter L Oakridge</p>
      <p class="contact__title">Vice President</p>
      <p class="contact__address">4427 Larkspur Crossing Way Suite<br>218 Larkhaven, NR 40217</p>
      <p class="contact__reach">pete@mvalq.com 555-418-7362</p>
    </div>
    <p class="company-name">Meridel Vantage Advisory</p>
  </section>

  <section class="card card--dark" aria-label="Business card, black">
    <div class="brand-mark">MVA</div>
    <div class="contact">
      <p class="contact__name">Peter L Oakridge</p>
      <p class="contact__title">Vice President</p>
      <p class="contact__address">4427 Larkspur Crossing Way Suite<br>218 Larkhaven, NR 40217</p>
      <p class="contact__reach">pete@mvalq.com 555-418-7362</p>
    </div>
    <p class="company-name">Meridel Vantage Advisory</p>
  </section>
</main>
</body>
</html>
```